Brackenfold Community Tennis needs a brochure & leaflet/poster designed!

We need a tri-fold A5 brochure and poster/flyer designed. Both designs should follow the same scheme and be designed so each can be used for different content. Colour scheme should be based around the the green on attached logo with contrast light grey. See colour scheme of examples attached, as this is the type of thing we are looking for, but using the green colour.

Tri-fold A5 Brochure - will become our information pamphlet to showcase Brackenfold Community Tennis. Attached is the current leaflet (we do not need a full page with online booking instructions though). We want a more fresh and modern look with a better front page. Need to include sections for a welcome introduction, how to book a court (simplified and shorter), Coaching (larger section for coaching), Cafe, Brackenfold Tennis Club and Local Tennis Leagues. It needs to be generic so we can in future update content when needed. I have also added a few brochures that we have found online, to give you a feel of the type of design we're looking for.

Poster/leaflet - a generic leaflet/poster that can be updated with current offers and info. Should include pictures, area for key message and contact details section at bottom. Include social media icons (FB, Twitter). Should follow the same scheme as all other material. Should be able to print in either A5/A4/A3

I have attached some pictures to use and the logo too.

Target Market(s)

Tennis, sports

Industry/Entity Type

Community

Font styles to use
Serif

Colors
00a990
aaaaaa
5c5c5c

Requirements
Must have
• Similar structure to the attached examples, giving you a feeling of the look and feel we are after!
Should not have
• Should not look like current brochure, need a full re-design

```html
<!DOCTYPE html>
<html lang="en">
<head>
<meta charset="utf-8">
<title>Brackenfold Community Tennis – Coaching Brochure</title>
<link rel="stylesheet" href="https://fonts.googleapis.com/css2?family=Roboto+Condensed:wght@300;400&family=Passion+One:wght@700&family=Archivo+Black&display=swap">
<style>
  :root{
    --teal:#00a990;
    --teal-dark:#007f6c;
    --teal-light:#2cc4a9;
    --grey-light:#e4e4e4;
    --grey-mid:#aaaaaa;
    --grey-dark:#5c5c5c;
    --charcoal:#3a3a3a;
    --ink:#2b2b2b;
    --white:#ffffff;
    --page-bg:#d9d6d2;
  }
  *{margin:0;padding:0;box-sizing:border-box}
  html,body{width:1200px;height:907px;overflow:hidden;background:var(--page-bg)}
  .brochure{position:absolute;left:87px;top:75px;width:1033px;height:735px;overflow:hidden;
    box-shadow:0 6px 18px rgba(0,0,0,.35)}
  .brochure-shapes{position:absolute;inset:0}

  .panel-title{position:absolute;left:37px;top:22px;font-family:"Passion One",sans-serif;
    font-size:54px;line-height:1;color:var(--teal);
    text-shadow:2px 2px 0 var(--charcoal),3px 3px 3px rgba(0,0,0,.4)}
  .brand-tag{position:absolute;display:flex;align-items:center;gap:6px;
    font-family:"Roboto Condensed",sans-serif;font-weight:400;color:var(--teal);line-height:1.05}
  .brand-tag .dot{flex:none;border-radius:50%;background:var(--teal)}
  .brand-tag--small{left:264px;top:20px;width:72px;height:68px;background:var(--white);
    padding:6px;font-size:9.5px;flex-direction:column;justify-content:center;text-align:center}
  .brand-tag--small .dot{width:18px;height:18px}
  .brand-tag--large{right:22px;top:22px;width:130px;flex-direction:column;text-align:center;font-size:13px}
  .brand-tag--large .dot{width:36px;height:36px}

  .photo{position:absolute;border-radius:18px}
  .photo--junior{left:30px;top:92px;width:272px;height:166px;transform:rotate(-3deg);
    border:4px solid var(--white);
    background:linear-gradient(135deg,#7d9a5c 0%,#b89a7a 45%,#3a5d8f 75%,#2d8ec9 100%)}
  .photo--group{left:430px;top:70px;width:566px;height:392px;transform:rotate(5deg);
    border:5px solid var(--teal);border-radius:34px;
    background:linear-gradient(120deg,#5b7f3e 0%,#8a6a5a 30%,#3e3e52 55%,#3b6fa8 78%,#c68e7a 100%)}

  .coaching-copy{position:absolute;left:20px;top:292px;width:316px;
    font-family:"Roboto Condensed",sans-serif;font-weight:300;font-size:14.6px;line-height:20px;
    color:var(--white);text-align:justify}
  .coaching-copy p{margin-bottom:20px}
  .coaching-copy .highlight{color:var(--teal-light)}

  .contact-block{position:absolute;left:398px;top:466px;width:284px;text-align:center;
    font-family:"Roboto Condensed",sans-serif;font-weight:400;font-size:15.4px;line-height:20px;color:var(--ink)}
  .contact-block .address{margin-bottom:20px}
  .contact-block .label{color:var(--teal-dark);font-weight:400}

  .slogan{position:absolute;left:690px;top:470px;width:330px;transform:rotate(-37deg);
    transform-origin:50% 50%;font-family:"Archivo Black",sans-serif;color:var(--white);
    font-size:52px;line-height:54px;letter-spacing:1px;
    text-shadow:1px 1px 0 #bdbdbd,2px 2px 0 #a8a8a8,3px 3px 0 #969696,4px 4px 0 #858585,5px 5px 0 #777,6px 6px 6px rgba(0,0,0,.35)}
  .slogan span{display:block}
  .slogan .line-2{padding-left:70px}
  .slogan .line-3{padding-left:10px}
</style>
</head>
<body>
<main class="brochure">
  <svg class="brochure-shapes" viewBox="0 0 1033 735" width="1033" height="735" aria-hidden="true">
    <defs>
      <linearGradient id="paperLeft" x1="0" x2="1"><stop offset="0" stop-color="#e2e2e2"/><stop offset="1" stop-color="#cfcfcf"/></linearGradient>
      <linearGradient id="paperMid" x1="0" x2="1"><stop offset="0" stop-color="#c9c9c9"/><stop offset=".25" stop-color="#f2f2f2"/><stop offset=".9" stop-color="#e6e6e6"/><stop offset="1" stop-color="#cfcfcf"/></linearGradient>
      <linearGradient id="paperRight" x1="0" x2="1"><stop offset="0" stop-color="#d4d4d4"/><stop offset=".4" stop-color="#f0f0f0"/><stop offset="1" stop-color="#dcdcdc"/></linearGradient>
      <linearGradient id="darkPanel" x1="0" x2="1"><stop offset="0" stop-color="#4a4a4a"/><stop offset=".6" stop-color="#5c5c5c"/><stop offset="1" stop-color="#8a8a8a"/></linearGradient>
      <linearGradient id="tealBand" x1="0" x2="1"><stop offset="0" stop-color="#007f6c"/><stop offset=".6" stop-color="#00a990"/><stop offset="1" stop-color="#2cc4a9"/></linearGradient>
      <linearGradient id="greyBand" x1="0" x2="1"><stop offset="0" stop-color="#5c5c5c"/><stop offset="1" stop-color="#aaaaaa"/></linearGradient>
    </defs>
    <rect x="0" y="0" width="353" height="735" fill="url(#paperLeft)"/>
    <rect x="353" y="0" width="340" height="735" fill="url(#paperMid)"/>
    <rect x="693" y="0" width="340" height="735" fill="url(#paperRight)"/>
    <polygon points="0,198 330,150 353,160 353,735 0,735" fill="url(#darkPanel)"/>
    <polygon points="353,160 400,220 400,735 353,735" fill="#3c3c3c"/>
    <polygon points="330,150 353,160 353,200 320,160" fill="#777"/>
    <polygon points="458,735 700,615 1033,615 1033,735" fill="url(#tealBand)"/>
    <polygon points="640,735 1033,395 1033,455 720,735" fill="url(#greyBand)"/>
    <polygon points="738,735 738,560 790,520 790,735" fill="#00927c"/>
    <polygon points="840,735 840,470 900,430 900,735" fill="#00a990"/>
    <polygon points="945,735 945,430 1033,400 1033,735" fill="#0fb79c"/>
    <line x1="693" y1="0" x2="693" y2="735" stroke="rgba(0,0,0,.08)" stroke-width="2"/>
  </svg>

  <h1 class="panel-title">coaching</h1>
  <div class="brand-tag brand-tag--small"><span class="dot"></span><span>Brackenfold Community Tennis</span></div>
  <div class="photo photo--junior" role="img" aria-label="Photo of a young boy in a blue jacket hitting a tennis ball on a court"></div>

  <section class="coaching-copy">
    <p>Our coaching programmes are run in partnership with Community Racket Association (CRA).</p>
    <p>We offer a number of coaching programmes from mini and junior tennis right through to adult beginner, intermediate and advanced coaching sessions. There are opportunities for either individual or group coaching sessions, alongside holiday camps run during the school holidays.</p>
    <p>All coaching follows a set programme designed by the NTB and CRA to ensure the best possible learning environments. We have a huge range of options available and there is something for everyone!</p>
    <p>For full details of our coaching programme please visit <span class="highlight">www.cratennis.org/brackenfold</span></p>
    <p>You can contact the coaching team on <span class="highlight">0800 555 0130</span> or email <span class="highlight">brackenfold@cratennis.org</span></p>
  </section>

  <div class="photo photo--group" role="img" aria-label="Photo of four smiling children looking through the strings of a large tennis racket"></div>

  <address class="contact-block" style="font-style:normal">
    <div class="address">Brackenfold Community Tennis<br>Holloway Recreation Ground<br>Elmsbrook Road, Brackenfold, BK2 4QT</div>
    <div><span class="label">t:</span> 01632 960495</div>
    <div><span class="label">e:</span> info@brackenfoldtennis.org.uk</div>
    <div><span class="label">w:</span> brackenfoldtennis.org.uk</div>
  </address>

  <div class="brand-tag brand-tag--large"><span class="dot"></span><span>Brackenfold Community Tennis</span></div>

  <p class="slogan"><span class="line-1">BOOK</span><span class="line-2">&amp; PLAY</span><span class="line-3">ENJOY</span></p>
</main>
</body>
</html>
```